Brochure, website and corporate stationary Design Project

Project scope:
1 x brochure (A4 insert) design
1 x brochure folder design (both external pages and one internal (there will be a few lines of text on the left inside page). The internal right side page will be a pocket for brochures (A4 inserts)
1 x corporate stationary pack (Business Card, logo (a proper logo file format needs to be produced), Letterhead and Envelope)
1 x concept design for our website. You dont need to do the coding. What you need to deliver is the design in a standard format (i.e. photoshop or blend)
Summary: the scope of the project is to design our brochure and its brochure folder, corporate stationary design and graphics concept design for our website. You should also consider our existing logo when performing the above design work (you can modify the logo slightly if you think it would improve look and feel and relevancy to overall design).
• We are a small IT services company
• The folder will be used to hold the brochures (inserts). The folder will be given to prospect customers (see attached a sample service brochure called “Fjällux User support services Ver0.1.docx”)
• On the cover of the folder, we want to have a design that uses keywords / phrases that reflects our main services (see attached file called “Phrases for presentation folder.docs”). Please note that not all phrases have to be used, use a logic in which ones or add new suggestions
• Inside the folder, at left side we want to have a short text explaining about our services a bit (see attached file called “Brochure Main section v0.91.docx”)
• All designs (corporate stationary, brochure, folder, web, etc.) must be consistent with each other and follow same concept, colour scheme, etc
• you are allowed to do minor changes to our existing logo if you have good reason to do so (see attached logo)
• We want our website design to be simple, elegant, not very colourful, light. HTML5. No flash. (you dont need to do the actual coding of the website, just deliver the design in Photoshop, Blend or any other standard format) With minimal menu items such as: home, services, about us, news, contact us, and other important ones if any. Same colour and design scheme as corporate stationary and brochures
• The company name “Fjällux” is derived from the Swedish word “Grön” (meaning green) and “teQ” which stands for technology but spelled with a “Q” to resemble Quality. The corporate green colour comes from the word “Grön”.
• All templates must be delivered in a standard editable format
Reason: To provide more time to the designers to come with their design submissions.
please note that we more than doubled the budget for this project
We deliver IT services to companies of 3-4 employees upto 200-300 employees. The brochures are intended for prospect customers (non IT people)
Business

```html
<!DOCTYPE html>
<html lang="en">
<head>
<meta charset="utf-8">
<title>Our Services</title>
<link rel="stylesheet" href="https://fonts.googleapis.com/css2?family=Arimo:ital,wght@1,400;1,700&display=swap">
<style>
  :root {
    --frame-green: #7cc243;
    --service-green: #8aab6c;
    --service-green-dark: #6f8f55;
    --page-bg: #f1f1ef;
    --ink: #111111;
    --number-ink: #3d3d3d;
    --white: #ffffff;
    --icon-grey: #7f9a86;
  }
  html, body { margin: 0; padding: 0; overflow: hidden; }
  body { width: 1200px; height: 800px; font-family: "Arimo", Arial, sans-serif; }
  .page {
    position: relative;
    width: 1200px; height: 800px;
    box-sizing: border-box;
    background: var(--page-bg);
    border-left: 20px solid var(--frame-green);
    border-right: 20px solid var(--frame-green);
    border-bottom: 16px solid var(--frame-green);
    overflow: hidden;
  }
  .hub {
    position: absolute; left: 486px; top: 50px;
    width: 248px; height: 248px; border-radius: 50%;
    background: var(--service-green);
    box-shadow: 0 0 0 4px var(--white), 0 2px 8px rgba(0,0,0,.25);
    display: flex; align-items: center; justify-content: center; text-align: center;
    color: var(--white); font-style: italic; font-weight: 700; font-size: 36px; line-height: 1.1;
    text-shadow: 2px 2px 3px rgba(0,0,0,.55);
  }
  .service-number {
    position: absolute; width: 84px; height: 84px; border-radius: 50%;
    background: var(--service-green);
    box-shadow: 0 0 0 3px var(--white), 0 2px 5px rgba(0,0,0,.2);
    display: flex; align-items: center; justify-content: center;
    font-style: italic; font-weight: 700; font-size: 46px; color: var(--number-ink);
    -webkit-text-stroke: 2px var(--white); paint-order: stroke fill;
  }
  .service-label {
    position: absolute; box-sizing: border-box;
    background: var(--service-green);
    box-shadow: 0 2px 4px rgba(0,0,0,.25);
    color: var(--white); font-style: italic; font-size: 22px; line-height: 1.25;
    display: flex; align-items: center; padding: 0 14px;
  }
  .service-label::after {
    content: ""; position: absolute; background: var(--service-green);
    width: 14px; height: 22px; top: 50%; margin-top: -11px;
  }
  .points-right::after { right: -14px; clip-path: polygon(0 0, 100% 50%, 0 100%); }
  .points-left::after { left: -14px; clip-path: polygon(100% 0, 0 50%, 100% 100%); }
  .points-up::after { top: -12px; left: 50%; margin: 0 0 0 -11px; width: 22px; height: 12px; clip-path: polygon(0 100%, 50% 0, 100% 100%); }
  .align-center { justify-content: center; text-align: center; }
  .contact-button {
    position: absolute; left: 80px; top: 460px; width: 246px; height: 46px;
    background: var(--frame-green); box-shadow: 0 2px 4px rgba(0,0,0,.3);
    display: flex; align-items: center; padding-left: 24px; box-sizing: border-box;
    font-style: italic; font-weight: 700; font-size: 26px; color: var(--ink);
  }
  .contact-button::after {
    content: ""; position: absolute; right: -10px; top: 13px; width: 10px; height: 20px;
    background: var(--frame-green); clip-path: polygon(0 0, 100% 50%, 0 100%);
  }
  .phone-icon { position: absolute; left: 522px; top: 500px; width: 76px; height: 70px; }
  .contact-info {
    position: absolute; left: 0; right: 0; top: 602px; text-align: center;
    font-style: italic; font-size: 21px; color: var(--ink); padding-right: 40px;
  }
</style>
</head>
<body>
<div class="page">
  <div class="service-label points-right" style="left:120px;top:20px;width:300px;height:64px;">IT Management<br>and Consultancy</div>
  <div class="service-label points-right" style="left:80px;top:116px;width:290px;height:110px;">Server, Telephony and Network Installation and Support</div>
  <div class="service-label points-right" style="left:204px;top:266px;width:206px;height:50px;">User Support</div>
  <div class="service-label points-up align-center" style="left:550px;top:400px;width:136px;height:44px;">Security</div>
  <div class="service-label points-left align-center" style="left:824px;top:244px;width:290px;height:112px;">Cloud Services – Email, Storage, Business Applications</div>
  <div class="service-label points-left align-center" style="left:866px;top:114px;width:288px;height:106px;">Business Applications i.e. CRM, ERP, Accounting software</div>
  <div class="service-label points-left" style="left:830px;top:40px;width:260px;height:48px;">App Development</div>

  <div class="hub">OUR<br>SERVICES</div>

  <div class="service-number" style="left:408px;top:34px;">1</div>
  <div class="service-number" style="left:368px;top:132px;">2</div>
  <div class="service-number" style="left:408px;top:238px;">3</div>
  <div class="service-number" style="left:562px;top:302px;">4</div>
  <div class="service-number" style="left:714px;top:238px;">5</div>
  <div class="service-number" style="left:754px;top:132px;">6</div>
  <div class="service-number" style="left:708px;top:34px;">7</div>

  <div class="contact-button">Contact us</div>

  <svg class="phone-icon" viewBox="0 0 76 70" aria-hidden="true">
    <path d="M4 22 C4 8 72 8 72 22 L72 28 L56 28 L56 20 L20 20 L20 28 L4 28 Z" fill="var(--icon-grey)"/>
    <path d="M22 26 L54 26 L66 46 L66 66 L10 66 L10 46 Z" fill="var(--icon-grey)"/>
    <circle cx="38" cy="46" r="11" fill="var(--page-bg)"/>
    <circle cx="38" cy="46" r="5" fill="var(--icon-grey)"/>
  </svg>

  <div class="contact-info">CONTACT INFO GOES HERE</div>
</div>
</body>
</html>
```